TOBREL Business Card Design

We need a business card design for a current Plastering company now moving to building and constructing new homes.
We have been in the Plastering(rendering) business for 15yrs and have made a good name with our customers for our Top Quality of work that we provide.
We would like TOBREL to be the main attraction with an image of architectural roof tops or house design within it. Blue Yellow and Black are colours we like but are willing to see other ideas.
We would like the design to be modern and communicate quality and experience.
Industry/Entity Type
Building
Contact Information for Business Card
TOBREL Building and Plastering
PO BOX 73519 Lakeview Northgate NT 0899
PH/Fax: 08 83170925 Email: tobrel@wavemail.example
Glen: 0419372654 Ruth:0408631597
ABN:57 208 931 446

```html
<!DOCTYPE html>
<html lang="en">
<head>
<meta charset="utf-8">
<title>TOBREL Building and Plastering – Business Card</title>
<link href="https://fonts.googleapis.com/css2?family=Open+Sans:wght@300;400;600;800&display=swap" rel="stylesheet">
<style>
  :root {
    --stage: #dfe4e7;
    --card-white: #fbfbfb;
    --brand-blue: #4296d4;
    --ink: #161616;
    --text-grey: #3a3a3a;
    --white: #ffffff;
  }
  * { margin: 0; padding: 0; box-sizing: border-box; }
  html, body {
    width: 1200px; height: 960px; overflow: hidden;
    background: var(--stage);
    font-family: "Open Sans", Arial, sans-serif;
  }
  .stage { position: relative; width: 1200px; height: 960px; }
  .card {
    position: absolute; left: 290px;
    width: 620px; height: 379px;
    border-radius: 3px;
    box-shadow: 0 6px 18px rgba(0,0,0,0.18);
    overflow: hidden;
  }
  .card--front { top: 71px; background: var(--card-white); }
  .card--back  { top: 510px; background: var(--brand-blue); }

  .brand {
    position: absolute; left: 0; right: 0;
    display: flex; flex-direction: column; align-items: center;
  }
  .card--front .brand { top: 44px; }
  .card--back .brand  { top: 128px; }
  .brand__row { display: flex; align-items: center; gap: 14px; }
  .brand__dot {
    width: 26px; height: 26px; border-radius: 50%;
    background: var(--brand-blue);
  }
  .card--back .brand__dot { background: var(--white); }
  .brand__name {
    font-weight: 800; font-size: 84px; line-height: 1;
    letter-spacing: 1px; color: var(--ink);
  }
  .brand__tagline {
    align-self: flex-end; margin-right: 150px; margin-top: 2px;
    font-weight: 800; font-size: 15px; letter-spacing: 0.5px;
    text-transform: uppercase; color: var(--ink);
  }

  .band {
    position: absolute; left: 0; right: 0; top: 172px; height: 44px;
    background: var(--brand-blue);
    color: var(--white); font-weight: 300; font-size: 24px; line-height: 44px;
  }
  .band__contact { position: absolute; top: 0; white-space: nowrap; }
  .band__contact--first { left: 110px; }
  .band__contact--second { left: 360px; }

  .contact-list {
    position: absolute; left: 70px; top: 262px;
    list-style: none; font-size: 14px; color: var(--text-grey);
  }
  .contact-list li { display: flex; align-items: center; gap: 14px; height: 30px; }
  .contact-list svg { width: 14px; height: 14px; fill: var(--brand-blue); }

  .postal {
    position: absolute; left: 370px; top: 238px;
    display: flex; gap: 10px;
    font-style: normal;
    font-size: 12px; line-height: 18px; color: var(--text-grey);
    text-transform: uppercase;
  }
  .postal svg { width: 12px; height: 12px; margin-top: 2px; fill: var(--brand-blue); flex: none; }
</style>
</head>
<body>
<main class="stage">

  <section class="card card--front" aria-label="Business card front">
    <header class="brand">
      <div class="brand__row">
        <span class="brand__name">TOBREL</span>
        <span class="brand__dot"></span>
      </div>
      <span class="brand__tagline">Building and Plastering</span>
    </header>

    <div class="band">
      <span class="band__contact band__contact--first">Glen: 0419372654</span>
      <span class="band__contact band__contact--second">Ruth:0408631597</span>
    </div>

    <ul class="contact-list">
      <li>
        <svg viewBox="0 0 24 24" aria-hidden="true"><path d="M6.6 10.8a15.1 15.1 0 0 0 6.6 6.6l2.2-2.2c.3-.3.7-.4 1-.2 1.1.4 2.3.6 3.6.6.6 0 1 .4 1 1V20c0 .6-.4 1-1 1A17 17 0 0 1 3 4c0-.6.4-1 1-1h3.5c.6 0 1 .4 1 1 0 1.3.2 2.5.6 3.6.1.3 0 .7-.2 1z"/></svg>
        <span>08 83170925</span>
      </li>
      <li>
        <svg viewBox="0 0 24 24" aria-hidden="true"><path d="M2 5h20v14H2zm2 2v.5l8 5 8-5V7zm0 2.8V17h16V9.8l-8 5z"/></svg>
        <span>tobrel@wavemail.example</span>
      </li>
    </ul>

    <address class="postal">
      <svg viewBox="0 0 24 24" aria-hidden="true"><path d="M12 3 2 12h3v8h5v-5h4v5h5v-8h3z"/></svg>
      <span>PO Box 73519 Lakeview<br>Northgate NT 0899<br>ABN:57 208 931 446</span>
    </address>
  </section>

  <section class="card card--back" aria-label="Business card back">
    <header class="brand">
      <div class="brand__row">
        <span class="brand__name">TOBREL</span>
        <span class="brand__dot"></span>
      </div>
      <span class="brand__tagline">Building and Plastering</span>
    </header>
  </section>

</main>
</body>
</html>
```